Lifecoach needs website design based on a standard Wordpress theme

I need a website for my new lifecoaching business that can be easily implemented in Wordpress, it needs to be compatible with a standard Wordpress theme. So I can place the pictures, texts etc. in a standard theme of Wordpress.

I want the design to be a very good feeling and playfull one, based on my logo.

Target Market(s)

I will coach people to reach their goals and dreams in life.

Industry/Entity Type

Business

Requirements
Must have
• Can be easy implemented in Wordpress.
Nice to have
• Photo's of nature are nice.

```html
<!DOCTYPE html>
<html lang="en">
<head>
<meta charset="utf-8">
<title>Tom van Aarde Lifecoach</title>
<link href="https://fonts.googleapis.com/css2?family=Arimo:ital,wght@0,400;0,700;1,700&family=Tinos&display=swap" rel="stylesheet">
<style>
:root{
  --navy:#0f4c7c;
  --navy-dark:#0a3a62;
  --sky:#6fa8dc;
  --sky-light:#cfe3f5;
  --mint:#c5dde0;
  --ink:#222;
  --muted:#8a8a8a;
  --title:#3e5670;
  --pink:#d98aa7;
  --grey:#7b7b7b;
  --lilac:#a68cc9;
  --sage:#b3bc97;
  --btn:#1b5fa6;
  --footer:#4b4b4b;
  --line:#dde4e6;
}
*{box-sizing:border-box;margin:0;padding:0}
html,body{width:1157px;height:1200px;overflow:hidden;background:#fff;font-family:"Arimo",Arial,sans-serif;color:var(--ink)}
.page{position:relative;width:965px;height:1001px;transform:scale(1.199);transform-origin:0 0;background:#f4f6f7}
.abs{position:absolute}
a{color:inherit}

/* header */
.header{left:0;top:0;width:965px;height:122px;background:linear-gradient(100deg,#e6f0fa 0%,#a9cbed 35%,#6fa3d8 70%,#8fbce6 100%);overflow:hidden}
.header .shine{position:absolute;right:80px;top:-40px;width:60px;height:200px;background:rgba(255,255,255,.25);transform:rotate(30deg)}
.header .shine.two{right:20px;width:30px}
.brand{left:14px;top:44px;display:flex;align-items:center;gap:8px}
.brand-mark{width:68px;height:68px;border-radius:50%;background:var(--navy);opacity:.85}
.brand-name{color:#1d5677;font-weight:700;font-size:21px;line-height:1;letter-spacing:.5px}
.brand-name span{display:block;font-size:13px;letter-spacing:1.5px;margin:3px 0 0 48px}
.nav{left:286px;top:82px;display:flex;gap:2px}
.nav a{display:block;width:134px;height:40px;line-height:42px;text-align:center;font-size:13px;text-decoration:none;color:#333;background:#fff;border-radius:12px 12px 0 0;border:1px solid #d7dde2;border-bottom:none}
.nav a.active{background:linear-gradient(#444,#1e1e1e);color:#fff;border-color:#222}

/* how panel */
.how{left:10px;top:132px;width:270px;height:281px;background:var(--navy);border-radius:5px;color:#fff;padding:14px 20px}
.how h2{font-weight:400;font-size:44px;line-height:1}
.how p{font-size:22px;line-height:26px}
.how hr{border:0;border-top:2px solid #fff;margin:10px 2px 16px 0}
.how ul{list-style:none;display:grid;grid-template-columns:137px 1fr;row-gap:9px;font-size:15px}
.how li{padding-left:16px;position:relative;height:21px;line-height:21px}
.how li::before{content:"›";position:absolute;left:0;color:#e77}
.how li.on{outline:1px solid #fff;border-radius:9px;outline-offset:4px;width:95px;margin-left:10px;padding-left:22px}
.how li.on::before{left:6px}
.how li:not(.on):nth-child(odd){margin-left:16px}

/* hero */
.hero{left:287px;top:132px;width:668px;height:244px;background:linear-gradient(#bcd8ef 0%,#e4eff7 60%,#9ccf5c 82%,#6fae35 100%)}
.hero-text{left:635px;top:176px;color:#34506e;font-weight:700}
.hero-text .l1{font-size:38px}
.hero-text .l1 small,.hero-text .l2 small{font-size:24px;font-weight:400}
.hero-text .l2{font-size:34px;margin-left:50px;line-height:34px}
.hero-text .l3{font-size:14px;margin-top:8px}
.cta{left:630px;top:288px;width:271px;height:52px;background:linear-gradient(#2d7cd0,#0f4d9a);border:1px solid #0a3a75;color:#fff;font-weight:700;font-size:19px;line-height:52px;text-align:center}
.topics{left:287px;top:376px;display:flex;height:37px;color:#fff;font-size:12px;font-weight:700}
.topics div{line-height:37px;text-align:center}
.topics .t1{width:164px;background:var(--pink)}
.topics .t2{width:173px;background:var(--grey)}
.topics .t3{width:168px;background:var(--lilac)}
.topics .t4{width:163px;background:var(--sage)}

/* boxes */
.box{background:#fff;border:1px solid var(--line);border-radius:6px;overflow:hidden}
.box-head{height:44px;background:var(--mint);display:flex;align-items:center;padding-left:14px;gap:10px;font-size:16px;color:#333}
.box-head i{width:13px;height:13px;border-radius:50%;background:#fff;border:1px solid #999;position:relative}
.box-head i::after{content:"";position:absolute;left:3px;top:4px;border:3px solid transparent;border-top:4px solid #333}
.item{padding:0 22px}
.item h4{font-size:12px;font-weight:700;text-decoration:underline;margin-bottom:10px}
.item p{font-size:12px;line-height:17px;color:var(--muted)}
.item p u{color:#777}
.more{font-size:12px;font-weight:700;margin-top:6px;color:var(--ink)}
.more::before{content:"» ";color:#999;font-weight:400}
.more a{text-decoration:underline}

.advice{left:11px;top:422px;width:268px;height:313px}
.subscribe{left:12px;top:745px;width:265px;height:190px;background:var(--navy);border-radius:6px;text-align:center;color:#fff}
.subscribe h3{font-weight:400;font-size:30px;text-decoration:underline;text-underline-offset:5px;margin-top:34px}
.signup{display:flex;margin:18px 12px 0 11px;height:26px;border-radius:13px;overflow:hidden;background:#fff}
.signup span{flex:1;text-align:left;color:#333;font-size:16px;line-height:26px;padding-left:10px}
.signup b{width:77px;background:linear-gradient(#4cc6f0,#1da6db);font-weight:400;color:#0b3a62;font-size:16px;line-height:26px}
.social{display:flex;gap:2px;justify-content:center;margin-top:20px}
.social i{width:28px;height:28px;border-radius:3px}

.center{left:288px;top:422px;width:388px;height:514px}
.welcome{height:158px;background:var(--mint);padding:18px 34px}
.welcome h3{font-weight:400;font-size:22px;color:var(--title)}
.welcome h5{font-weight:400;font-size:13px;color:var(--title);text-decoration:underline;margin:6px 0 10px}
.welcome p{font-size:12.5px;line-height:17px;color:#333}
.guide{padding:20px 34px}
.guide h2{font-family:"Tinos",serif;font-weight:400;font-size:30px;color:var(--title)}
.guide h4{font-family:"Tinos",serif;font-weight:400;font-size:15px;color:var(--title);margin:22px 0 10px}
.guide p{font-size:11.5px;line-height:17px;color:var(--muted)}
.guide hr{border:0;border-top:1px solid var(--line);margin:16px -18px 0}
.readmore{display:inline-block;margin-top:24px;width:103px;height:26px;border-radius:13px;background:var(--title);color:#fff;font-size:12px;font-weight:700;line-height:26px;text-align:center}

.testi{left:685px;top:422px;width:269px;height:266px}
.testi-photo{margin:21px 0 0 28px;width:210px;height:96px;border-radius:8px;border:1px solid #bbb;background:linear-gradient(90deg,#c9d2dc,#6d7480 50%,#2a2d33)}
.testi .who{font-style:italic;font-weight:700;font-size:13px;margin:20px 0 6px 32px}
.testi p{font-size:11.5px;line-height:16px;color:var(--muted);padding:0 32px}
.testi .more{padding-left:32px}

.articles{left:685px;top:702px;width:269px;height:234px}
.articles ul{list-style:none;margin:18px 0 0 32px}
.articles li{font-size:12px;font-weight:700;text-decoration:underline;height:22.7px;position:relative;padding-left:12px}
.articles li::before{content:"";position:absolute;left:0;top:5px;width:4px;height:4px;background:#222;border-radius:50%}

.footer{left:0;top:944px;width:965px;height:57px;background:linear-gradient(#3d3d3d,#5a5a5a);color:#ccc;font-size:11.5px;padding:25px 33px}
.footer a{color:#fff;text-decoration:underline}
</style>
</head>
<body>
<div class="page">

  <header class="header abs">
    <div class="shine"></div><div class="shine two"></div>
  </header>
  <div class="brand abs">
    <div class="brand-mark"></div>
    <div class="brand-name">TOM VAN AARDE<span>LIFECOACH</span></div>
  </div>
  <nav class="nav abs">
    <a class="active">About us</a><a>Coaching</a><a>Our Training</a><a>Our Articles</a><a>Contact us</a>
  </nav>

  <section class="how abs">
    <h2>How</h2>
    <p>Do You What<br>to Improve your Life?</p>
    <hr>
    <ul>
      <li class="on">Work</li><li>Peace</li>
      <li>Social Life</li><li>Family</li>
      <li>Partner</li><li>Friends</li>
      <li>Dreams</li><li>Others</li>
    </ul>
  </section>

  <div class="hero abs" role="img" aria-label="Happy young woman holding flowers with arms wide open in a green meadow under a bright sky"></div>
  <div class="hero-text abs">
    <div class="l1">Enjoy <small>life</small></div>
    <div class="l2"><small>Get</small> happy <small>now</small></div>
    <div class="l3">24/7 life advice from TOP Life Coaches</div>
  </div>
  <div class="cta abs">Click here to motivate now</div>
  <div class="topics abs">
    <div class="t1">Set Powerful Goals</div>
    <div class="t2">Building Confidence</div>
    <div class="t3">Overcoming Inertia</div>
    <div class="t4"><u>Free!</u> Coaching</div>
  </div>

  <section class="advice box abs">
    <div class="box-head"><i></i>Advice For Happy Life</div>
    <div class="item" style="margin-top:26px">
      <h4>The 7 Rules Of Success</h4>
      <p><u>Sed ut perspiciat unde</u> omikas miaset lerode feratersia accusa ntium rekertsdea vitae dicta suntasea explicabo.</p>
      <div class="more"><a>read more</a></div>
    </div>
    <div class="item" style="margin-top:30px">
      <h4>Student Life Coaches</h4>
      <p><u>Sed ut perspiciat unde</u> omikas miaset lerode feratersia accusa ntium rekertsdea vitae dicta suntasea explicabo.</p>
      <div class="more"><a>read more</a></div>
    </div>
  </section>

  <section class="subscribe abs">
    <h3>Subscribe Now</h3>
    <div class="signup"><span>Email</span><b>Now</b></div>
    <div class="social">
      <i style="background:#2a9fd8"></i><i style="background:#444"></i><i style="background:#3b5a99"></i><i style="background:#f39a1e"></i>
    </div>
  </section>

  <section class="center box abs">
    <div class="welcome">
      <h3>Welcome Message</h3>
      <h5>Cum Socis natoque peibu partu dawsabertase</h5>
      <p>nasmonlase dusce hertserno lorem ipsumadio fertase orbuis ultricies pharetra magna onec accumsan males uadanec simet erorm idolor sit aconseuer adipiscing.</p>
    </div>
    <div class="guide">
      <h2>Guide to Life Coaching</h2>
      <h4>What is life coaching?</h4>
      <p>Masnd flinest mikaia setareas mias lerode feratersia ausa ntium rekaesdea ntiumas totarp billose miaserset lesavitae dicta sunt explicabo. Nemo enim ipsam volupt atequia Inventore veritatis etchitecto beatae!</p>
      <hr>
      <h4>Where can i find a reputable coach ?</h4>
      <p>Merspiciat undmikaia setareas mias erode feratersia ntiumas otarp billos miaserset lesa vitae dicta sunt, explicabo nemo beatae voluptas sit, aspernatur aut odit .</p>
      <div class="readmore">READ MORE</div>
    </div>
  </section>

  <section class="testi box abs">
    <div class="box-head"><i></i>Testimonials</div>
    <div class="testi-photo" role="img" aria-label="Smiling businessman and businesswoman standing in an office"></div>
    <div class="who">Martin Hollis, manager</div>
    <p>Ferode feratersia ausa ntium resdea ntiumas totarp billose.</p>
    <div class="more"><a>more testimonials</a></div>
  </section>

  <section class="articles box abs">
    <div class="box-head"><i></i>Self Help Articles</div>
    <ul>
      <li>Past Predicts Future?</li>
      <li>The Time Of Your Life</li>
      <li>Brain Re-Programming - Your Norms</li>
      <li>How to Find Love</li>
      <li>Self Tests</li>
      <li>Buying Happiness</li>
      <li>Your True Purpose</li>
    </ul>
  </section>

  <footer class="footer abs">Life Coach © 2009. <a>Privacy policy</a></footer>
</div>
</body>
</html>
```